Dr. Marissa Tevlin Medical/Chiropractic Business Card

Dr. Tevlin is a chiropractor and will require a business card that she uses every single day to book appointments on the back side of the card. Currently the office name goes by Dr. Marissa Tevlin. The chiropractic profession is based on the diagnosis and manipulative treatment of misalignments of the joints, especially those of the spinal column, which are held to cause other disorders by affecting the nerves, muscles, and organs. Dr. Marissa Tevlin is looking for a contemporary and minimalistic design.

Industry/Entity Type

Medical

Contact Information for Business Card

Name: Dr. Marissa Tevlin; Address: 748 Harcastle Rd South, London, ON N5R 2K7; Phone Number: 519.274.6193; Fax: 519.281.5046; email: marissa.tevlin@quorvamail.com

Requirements
Must have
• ability to write multiple appointments date/time on the back of card

```html
<!DOCTYPE html>
<html lang="en">
<head>
<meta charset="utf-8">
<title>Dr. Marissa Tevlin – Business Card</title>
<link href="https://fonts.googleapis.com/css2?family=Raleway:wght@400;500;800&display=swap" rel="stylesheet">
<style>
  :root {
    --teal: #3b8474;
    --ink: #221f20;
    --white: #ffffff;
    --slot: #e7e7e7;
    --stage: #d9d9d6;
  }
  * { box-sizing: border-box; margin: 0; padding: 0; }
  html, body { width: 1200px; height: 900px; overflow: hidden; }
  body {
    background: var(--stage);
    font-family: "Raleway", sans-serif;
    position: relative;
  }

  /* ---------- Front ---------- */
  .card-front {
    position: absolute;
    left: 60px; top: 273px;
    width: 620px; height: 354px;
    background: var(--ink);
    box-shadow: 0 8px 24px rgba(0,0,0,.25);
    overflow: hidden;
  }
  .front-band {
    height: 100px;
    background: var(--teal);
    border-bottom: 4px solid var(--white);
    text-align: center;
    padding-top: 24px;
  }
  .doctor-name {
    color: var(--white);
    font-weight: 500;
    font-size: 40px;
    line-height: 1;
    letter-spacing: .5px;
  }
  .doctor-title {
    color: var(--ink);
    font-size: 15px;
    line-height: 18px;
    letter-spacing: 1px;
    margin-top: 4px;
  }
  .front-body { text-align: center; padding-top: 16px; }
  .address {
    color: var(--teal);
    font-size: 19px;
    line-height: 1.25;
    font-weight: 500;
  }
  .contact-list { list-style: none; margin-top: 14px; }
  .contact-item {
    display: flex; align-items: center; justify-content: center;
    gap: 14px;
    color: var(--white);
    font-size: 21px;
    height: 38px;
  }
  .contact-icon {
    width: 32px; height: 32px; border-radius: 50%;
    background: var(--teal);
    display: flex; align-items: center; justify-content: center;
    flex: none;
  }

  /* ---------- Back ---------- */
  .card-back {
    position: absolute;
    left: 770px; top: 140px;
    width: 354px; height: 620px;
    background: var(--ink);
    box-shadow: 0 8px 24px rgba(0,0,0,.25);
    padding: 30px 30px 0;
    overflow: hidden;
  }
  .appointments-title {
    color: var(--teal);
    font-weight: 800;
    font-size: 34px;
    line-height: 40px;
    letter-spacing: .5px;
    text-align: center;
  }
  .column-labels {
    display: grid; grid-template-columns: 1fr 1fr;
    color: var(--white);
    font-size: 24px;
    line-height: 30px;
    margin-top: 4px;
    padding: 0 22px;
  }
  .column-labels span:last-child { text-align: right; }
  .slot-table {
    margin-top: 10px;
    background: var(--slot);
    padding: 8px;
    display: grid;
    grid-template-columns: 1.25fr 1fr;
    grid-template-rows: repeat(9, 38px);
    gap: 6px 14px;
  }
  .slot { border: 2px solid var(--ink); background: var(--slot); }
  .reschedule-note {
    color: var(--white);
    font-size: 15px;
    line-height: 18px;
    margin-top: 14px;
    padding-left: 4px;
  }
</style>
</head>
<body>

<section class="card-front">
  <header class="front-band">
    <h1 class="doctor-name">Dr. Marissa Tevlin</h1>
    <p class="doctor-title">CHIROPRACTOR</p>
  </header>
  <div class="front-body">
    <p class="address">748 Harcastle Rd South<br>London, ON N5R 2K7</p>
    <ul class="contact-list">
      <li class="contact-item">
        <span class="contact-icon">
          <svg width="16" height="16" viewBox="0 0 24 24"><path fill="#fff" d="M6.6 10.8a15 15 0 0 0 6.6 6.6l2.2-2.2c.3-.3.7-.4 1-.2 1.1.4 2.3.6 3.6.6.6 0 1 .4 1 1V20c0 .6-.4 1-1 1A17 17 0 0 1 3 4c0-.6.4-1 1-1h3.5c.6 0 1 .4 1 1 0 1.3.2 2.5.6 3.6.1.3 0 .7-.2 1z"/></svg>
        </span>519.274.6193
      </li>
      <li class="contact-item">
        <span class="contact-icon">
          <svg width="16" height="16" viewBox="0 0 24 24"><rect x="3" y="8" width="18" height="12" rx="1" fill="#fff"/><rect x="6" y="3" width="12" height="6" fill="#fff"/><rect x="6" y="11" width="8" height="1.5" fill="#3b8474"/><rect x="6" y="14" width="8" height="1.5" fill="#3b8474"/><rect x="16" y="11" width="2" height="5" fill="#3b8474"/></svg>
        </span>Fax: 519.281.5046
      </li>
      <li class="contact-item">
        <span class="contact-icon">
          <svg width="16" height="16" viewBox="0 0 24 24"><rect x="2" y="5" width="20" height="14" fill="#fff"/><path d="M2 5l10 8 10-8" fill="none" stroke="#3b8474" stroke-width="2"/></svg>
        </span>marissa.tevlin@quorvamail.com
      </li>
    </ul>
  </div>
</section>

<section class="card-back">
  <h2 class="appointments-title">APPOINTMENTS</h2>
  <div class="column-labels"><span>Date</span><span>Time</span></div>
  <div class="slot-table">
    <div class="slot"></div><div class="slot"></div>
    <div class="slot"></div><div class="slot"></div>
    <div class="slot"></div><div class="slot"></div>
    <div class="slot"></div><div class="slot"></div>
    <div class="slot"></div><div class="slot"></div>
    <div class="slot"></div><div class="slot"></div>
    <div class="slot"></div><div class="slot"></div>
    <div class="slot"></div><div class="slot"></div>
    <div class="slot"></div><div class="slot"></div>
  </div>
  <p class="reschedule-note">If you are unable to<br>make your appointment,<br>please call us to reschedule</p>
</section>

</body>
</html>
```